Business Card

Company: Willow Ridge Nursery.

Use uploaded logo or design one just like it. This is a tree growing operation and really like earth tone colors.

Target Market(s)

Landscaping company's, retail nurseries, and landscape arc.

Industry/Entity Type

Business

Font styles to use
Serif

Requirements
Must have
• Name: Dale Whitford
Title: Owner
Address: 48217 W. 150 Road, Grove, OK 74592
Office: 918-555-3172
Cell: 918-555-6094
Fax: 918-555-4418
email: dalewr@plainsmail.net
Willow Ridge Nursery

```html
<!DOCTYPE html>
<html lang="en">
<head>
<meta charset="utf-8">
<title>Willow Ridge Nursery – Business Card</title>
<link href="https://fonts.googleapis.com/css2?family=Roboto+Slab:wght@400;800&display=swap" rel="stylesheet">
<style>
  :root {
    --card-white: #ffffff;
    --forest: #117040;
    --sage-tint: #dbe9df;
    --sage-deep: #b9d3c1;
    --ink-light: #ffffff;
  }
  html, body {
    margin: 0;
    padding: 0;
    width: 1200px;
    height: 695px;
    overflow: hidden;
    background: var(--card-white);
  }
  .card {
    position: relative;
    width: 1200px;
    height: 695px;
    background: var(--card-white);
    font-family: "Roboto Slab", Georgia, serif;
    color: var(--ink-light);
  }
  .tree-art {
    position: absolute;
    left: 85px;
    top: 64px;
    width: 258px;
    height: 462px;
    border-radius: 46% 46% 30% 30% / 40% 40% 18% 18%;
    background: radial-gradient(ellipse at 50% 35%, var(--sage-tint), var(--sage-deep));
  }
  .info-panel {
    position: absolute;
    left: 424px;
    top: 0;
    width: 776px;
    height: 695px;
    background: var(--forest);
  }
  .line {
    position: absolute;
    left: 530px;
    margin: 0;
    white-space: nowrap;
    line-height: 1;
  }
  .owner-name, .owner-title {
    font-weight: 800;
    font-size: 45px;
    letter-spacing: 1px;
  }
  .owner-name { top: 70px; }
  .owner-title { top: 134px; }
  .company {
    top: 206px;
    font-size: 35px;
    font-weight: 400;
  }
  .contact {
    font-size: 35px;
    font-weight: 400;
  }
  .contact .label {
    display: inline-block;
    width: 44px;
    font-weight: 800;
  }
  .contact .colon {
    display: inline-block;
    width: 58px;
  }
  .contact-phone { top: 311px; }
  .contact-mobile { top: 363px; }
  .contact-fax { top: 418px; }
  .contact-email { top: 465px; }
  .address {
    font-size: 35px;
    font-weight: 400;
  }
  .address-street { top: 562px; }
  .address-city { top: 615px; }
</style>
</head>
<body>
  <div class="card">
    <div class="tree-art" role="img" aria-label="Hand-drawn sketch of a leafy tree with a root ball and a small shrub beside it"></div>

    <div class="info-panel"></div>

    <p class="line owner-name">Dale Whitford</p>
    <p class="line owner-title">Owner</p>
    <p class="line company">Willow Ridge Nursery</p>

    <p class="line contact contact-phone"><span class="label">P</span><span class="colon">:</span>918-555-3172</p>
    <p class="line contact contact-mobile"><span class="label">M</span><span class="colon">:</span>918-555-6094</p>
    <p class="line contact contact-fax"><span class="label">F</span><span class="colon">:</span>918-555-4418</p>
    <p class="line contact contact-email"><span class="label">E</span><span class="colon">:</span>dalewr@plainsmail.net</p>

    <p class="line address address-street">48217 W. 150 Road,</p>
    <p class="line address address-city">Grove, OK 74592</p>
  </div>
</body>
</html>
```